Business Card

We need some ideas for corporate business cards. I'm interested in a double sided card, with one side featuring our corporate logo, the other side with employee information.

Corporate colors, logo etc. available at www.brivalo.com

Industry/Entity Type

Business

Requirements
Must have
• The "Brivalo" logo with stylized "O"

Nice to have
• Preferred font is calibri

```html
<!DOCTYPE html>
<html lang="en">
<head>
<meta charset="utf-8">
<title>Brivalo Business Card</title>
<link rel="stylesheet" href="https://fonts.googleapis.com/css2?family=Mulish:ital,wght@0,400;0,600;0,700;1,400&family=PT+Serif&display=swap">
<style>
  :root {
    --page-bg: #ffffff;
    --label-grey: #9a9a9a;
    --blue-deep: #14226e;
    --blue-mid: #1f4fae;
    --blue-bright: #2f6fd0;
    --band-light: #e4e4e6;
    --band-mid: #c9c9cc;
    --band-edge: #2a2f4a;
    --brand-blue: #3e5a96;
    --silver-light: #f1f1f2;
    --silver-mid: #c6c6c9;
    --silver-dark: #8d8e99;
    --edge-navy: #2c3050;
    --ink: #111111;
    --ghost: #cfcfd2;
  }
  * { box-sizing: border-box; margin: 0; padding: 0; }
  html, body {
    width: 1200px; height: 682px; overflow: hidden;
    background: var(--page-bg);
  }
  .sheet { position: relative; width: 1200px; height: 682px; }

  .side-label {
    position: absolute; left: 62px;
    font-family: "PT Serif", serif;
    font-size: 17px; letter-spacing: 0.6px;
    color: var(--label-grey);
  }
  .side-label--front { top: 28px; }
  .side-label--back { top: 347px; }

  .card {
    position: absolute; left: 62px; width: 574px; height: 255px;
    border: 1px solid #1b1b1b;
    box-shadow: 9px 9px 7px rgba(0,0,0,0.55);
    overflow: hidden;
  }
  .card--front { top: 62px; }
  .card--back { top: 383px; }

  /* Front */
  .front-backdrop {
    position: absolute; inset: 0;
    background:
      radial-gradient(ellipse at 30% 15%, var(--blue-bright) 0%, transparent 55%),
      radial-gradient(ellipse at 75% 85%, var(--blue-bright) 0%, transparent 50%),
      linear-gradient(180deg, var(--blue-mid) 0%, var(--blue-deep) 100%);
  }
  .front-band {
    position: absolute; left: 0; right: 0; top: 90px; height: 60px;
    background: linear-gradient(90deg, var(--band-mid) 0%, var(--band-light) 30%, #f2f2f3 55%, var(--band-mid) 100%);
    border-top: 3px solid var(--band-edge);
    border-bottom: 3px solid var(--band-edge);
    box-shadow: 0 -4px 6px rgba(120,150,220,0.45), 0 4px 6px rgba(120,150,220,0.45);
  }
  .front-brand {
    position: absolute; left: 82px; top: 2px;
    display: flex; align-items: center; gap: 10px;
    font-family: "Mulish", sans-serif; font-weight: 700;
    font-size: 50px; line-height: 54px; letter-spacing: 3px;
    color: var(--brand-blue);
  }
  .brand-square {
    width: 30px; height: 30px; background: var(--brand-blue);
  }

  /* Back */
  .back-backdrop {
    position: absolute; inset: 0;
    background:
      radial-gradient(ellipse at 38% 55%, #ffffff 0%, var(--silver-light) 25%, transparent 70%),
      linear-gradient(180deg, var(--silver-mid) 0%, #e3e3e5 50%, var(--silver-mid) 100%);
  }
  .back-edge {
    position: absolute; left: 0; right: 0; height: 12px;
    background: linear-gradient(90deg, #e8e8ea 0%, var(--silver-dark) 35%, var(--edge-navy) 50%, var(--silver-dark) 65%, #e8e8ea 100%);
  }
  .back-edge--top { top: 0; }
  .back-edge--bottom { bottom: 0; }
  .back-ghost-brand {
    position: absolute; left: 18px; top: 24px;
    font-family: "Mulish", sans-serif; font-weight: 400;
    font-size: 70px; line-height: 70px; letter-spacing: 12px;
    color: var(--ghost);
  }
  .contact {
    position: absolute; left: 0; width: 500px; top: 112px;
    text-align: center;
    font-family: "Mulish", sans-serif; color: var(--ink);
  }
  .contact-name { font-size: 20px; font-weight: 700; line-height: 24px; }
  .contact-title { font-size: 18px; font-style: italic; line-height: 22px; margin-bottom: 8px; }
  .contact-line { font-size: 13px; line-height: 21px; }
</style>
</head>
<body>
<main class="sheet">
  <p class="side-label side-label--front">BUSINESS CARD FRONT</p>
  <section class="card card--front" aria-label="Business card front">
    <div class="front-backdrop" role="img" aria-label="Deep blue background with flowing wire-mesh waves"></div>
    <div class="front-band">
      <div class="front-brand"><span class="brand-square"></span>BRIVALO</div>
    </div>
  </section>

  <p class="side-label side-label--back">BUSINESS CARD BACK</p>
  <section class="card card--back" aria-label="Business card back">
    <div class="back-backdrop" role="img" aria-label="Silver background with a bright light burst of streaking panels"></div>
    <div class="back-edge back-edge--top"></div>
    <div class="back-edge back-edge--bottom"></div>
    <div class="back-ghost-brand">BRIVALO</div>
    <div class="contact">
      <p class="contact-name">Employee Name</p>
      <p class="contact-title">Title here</p>
      <p class="contact-line">5555 Street Address | City, ST 5555</p>
      <p class="contact-line">Direct: 555.555.5555 Mobile: 555.555.5555 Fax: 555.555.5555</p>
      <p class="contact-line">emplyee@email.com | brivalo.com</p>
    </div>
  </section>
</main>
</body>
</html>
```